Postcard/Poster design for Feature film

I'm just wrapping post-production on my indie first feature, and I'm going to be attending some big festivals over the next few months to promote my film by handing out postcards.

I'll also be needing posters for festivals that I'll get into.

The name of my film is Nettle Winter, and it's a melancholic drama about one woman's desperate need for a male child.
I have a still photo from the film that I'd like to use on the poster and postcard.
Updates

The postcard design should take into consideration the fact that a postcard has two sides. All the info doesnt have to on the front. Therefore the post card design should be two designs, the front and the back.
Take a look at a real postcard for inspiration.

Target Market(s)

The arthouse film loving types.

Requirements
Must have
• The design must have the still photo from the film, the name of the film, Nettle Winter, and all the other logo's at the bottom.
There are other logos that I'm unable to attach because I reached the limit, but I can send those later.

The postcard design should take into consideration the fact that a postcard has two sides. All the info doesn't have to be on the front of the card. Therefore the post card design should be in two parts, the front and the back.

The postcard size is standard (4 x 6 inches).
Poster 40 inches (wide) x 30 inches (high).

The design must be 350dpi.

```html
<!DOCTYPE html>
<html lang="en">
<head>
<meta charset="utf-8">
<title>Nettle Winter — Poster and Postcard Set</title>
<link rel="stylesheet" href="https://fonts.googleapis.com/css2?family=Courier+Prime:wght@400;700&family=Andika&family=Pathway+Gothic+One&family=Montserrat:wght@500&display=swap">
<style>
:root{
  --paper:#ffffff;
  --ink-black:#050403;
  --title-white:#f4f1ec;
  --title-brown:#86634a;
  --title-grey:#3d3935;
  --credit-light:#d9d4cd;
  --credit-dark:#4a4642;
  --rule-brown:#6e4b39;
  --shadow:rgba(0,0,0,.28);
}
*{box-sizing:border-box;margin:0;padding:0}
html,body{width:1200px;height:1005px;overflow:hidden;background:var(--paper)}
.sheet{position:relative;width:1200px;height:1005px}
.piece{position:absolute;overflow:hidden;box-shadow:0 1px 5px var(--shadow);background:var(--ink-black)}
.poster-portrait{left:37px;top:40px;width:383px;height:542px}
.poster-landscape{left:436px;top:40px;width:722px;height:542px}
.postcard-front{left:49px;top:602px;width:538px;height:358px}
.postcard-back{left:605px;top:602px;width:539px;height:358px;background:var(--paper)}

.still{position:absolute;inset:0;
  background:
    radial-gradient(ellipse 30% 40% at 62% 30%, rgba(120,80,55,.85), rgba(120,80,55,0) 70%),
    radial-gradient(ellipse 35% 25% at 75% 70%, rgba(200,110,100,.75), rgba(200,110,100,0) 70%),
    linear-gradient(90deg,#070605 0%,#1c1510 22%,#5a3f2c 45%,#b9a99a 70%,#e6e3dd 100%);}
.still::after{content:"";position:absolute;inset:0;background:linear-gradient(180deg,rgba(0,0,0,0) 55%,var(--ink-black) 88%)}
.postcard-front .still::after{background:linear-gradient(90deg,rgba(0,0,0,.6) 0%,rgba(0,0,0,0) 40%)}

.festival-mark{position:absolute;display:flex;align-items:center;gap:5px;font-family:'Montserrat',sans-serif;color:var(--ink-black);line-height:1.05}
.festival-mark .dot{width:11px;height:11px;border-radius:50%;background:var(--ink-black)}
.festival-mark small{display:block;font-size:.62em;letter-spacing:.04em}
.poster-portrait .festival-mark{right:20px;top:36px;font-size:12px}
.poster-landscape .festival-mark{right:26px;top:56px;font-size:15px}
.postcard-front .festival-mark{right:20px;top:34px;font-size:12px}

.title{position:absolute;line-height:.9;white-space:nowrap}
.title .line-top{display:block;font-family:'Courier Prime',monospace;font-weight:700;color:var(--title-white)}
.title .line-main{display:block;font-family:'Andika',sans-serif;color:var(--title-brown)}
.title .byline{display:block;margin-top:8px;font-family:'Pathway Gothic One',sans-serif;font-size:11px;letter-spacing:.05em;color:var(--title-white);text-transform:uppercase}
.poster-portrait .title{left:118px;top:352px}
.poster-portrait .line-top{font-size:28px}
.poster-portrait .line-main{font-size:42px}
.poster-portrait .byline{font-size:7px;margin-top:6px}
.poster-landscape .title{left:86px;top:190px}
.poster-landscape .line-top{font-size:48px}
.poster-landscape .line-main{font-size:76px}
.postcard-front .title{left:48px;top:112px}
.postcard-front .line-top{font-size:38px}
.postcard-front .line-main{font-size:60px}
.postcard-back .title{left:56px;top:118px}
.postcard-back .line-top{font-size:34px;color:var(--title-grey)}
.postcard-back .line-main{font-size:52px}
.postcard-back .byline{color:var(--title-grey);font-size:10px}

.credits{position:absolute;font-family:'Pathway Gothic One',sans-serif;text-transform:uppercase;color:var(--credit-light);line-height:1.35;letter-spacing:.02em}
.credits b{font-weight:400;font-size:1.3em;color:inherit}
.poster-portrait .credits{left:30px;right:30px;top:445px;font-size:5px;text-align:center}
.poster-landscape .credits{left:160px;width:400px;top:446px;font-size:7.5px;text-align:center}
.postcard-back .credits{left:292px;width:228px;top:128px;font-size:6.2px;line-height:1.3;color:var(--credit-dark)}
.postcard-back .credits b{font-size:1.25em}

.partners{position:absolute;display:flex;align-items:center;justify-content:space-between;font-family:'Pathway Gothic One',sans-serif;text-transform:uppercase;color:var(--credit-light)}
.partners span{display:flex;align-items:center;gap:3px}
.partners i{display:inline-block;width:7px;height:7px;background:currentColor}
.poster-portrait .partners{left:30px;right:30px;top:506px;font-size:7px}
.poster-landscape .partners{left:125px;right:125px;top:498px;font-size:10px}
.postcard-back .partners{left:292px;width:215px;top:214px;font-size:7px;color:var(--credit-dark)}

.divider{position:absolute;left:270px;top:23px;width:2px;height:312px;background:var(--rule-brown)}
</style>
</head>
<body>
<main class="sheet">

  <section class="piece poster-portrait">
    <div class="still" role="img" aria-label="Film still: a woman in a pink top sits by a bright window, gazing out, a child's arm around her"></div>
    <div class="festival-mark"><span class="dot"></span><span>Atelier Lumen<small>LA MAISON</small></span></div>
    <h1 class="title"><span class="line-top">Nettle</span><span class="line-main">Winter</span><span class="byline">A film by Ada Nwosu</span></h1>
    <p class="credits"><b>Quiet Field Pictures</b> presents a film by <b>Ada Nwosu</b> 'Nettle Winter' cinematographer <b>Irena Sowa</b><br>production designer <b>Daniel Osei Mensah</b> original music by <b>Karl Weidner</b> edited by <b>Paul Marchand</b> executive producer <b>Nkem Obi</b><br>executive producers <b>Efe Tobore, Ngozi Tobore, Samuel Tobore, Kemi Tobore, Tunde Ade, Ibim Dagogo, Sotonye Dagogo</b><br>producer <b>Ada Nwosu</b> and <b>Ola Tobore</b> director/writer <b>Ada Nwosu</b></p>
    <div class="partners"><span><i></i>Lensworks</span><span><i></i>Darkroom</span><span><i></i>Huelab</span><span><i></i>Quiet Field</span></div>
  </section>

  <section class="piece poster-landscape">
    <div class="still" role="img" aria-label="Film still: a woman in a pink top sits by a bright window, gazing out, a child's arm around her"></div>
    <div class="festival-mark"><span class="dot"></span><span>Atelier Lumen<small>LA MAISON</small></span></div>
    <h1 class="title"><span class="line-top">Nettle</span><span class="line-main">Winter</span><span class="byline">A film by Ada Nwosu</span></h1>
    <p class="credits"><b>Quiet Field Pictures</b> presents a film by <b>Ada Nwosu</b> 'Nettle Winter' cinematographer <b>Irena Sowa</b><br>production designer <b>Daniel Osei Mensah</b> original music by <b>Karl Weidner</b> edited by <b>Paul Marchand</b> executive producer <b>Nkem Obi</b><br>executive producers <b>Efe Tobore, Ngozi Tobore, Samuel Tobore, Kemi Tobore, Tunde Ade, Ibim Dagogo, Sotonye Dagogo</b><br>producer <b>Ada Nwosu</b> and <b>Ola Tobore</b> director/writer <b>Ada Nwosu</b></p>
    <div class="partners"><span><i></i>Lensworks</span><span><i></i>Darkroom</span><span><i></i>Huelab</span><span><i></i>Quiet Field</span></div>
  </section>

  <section class="piece postcard-front">
    <div class="still" role="img" aria-label="Film still: a woman in a pink top sits by a bright window, gazing out, a child's arm around her"></div>
    <div class="festival-mark"><span class="dot"></span><span>Atelier Lumen<small>LA MAISON</small></span></div>
    <h1 class="title"><span class="line-top">Nettle</span><span class="line-main">Winter</span><span class="byline">A film by Ada Nwosu</span></h1>
  </section>

  <section class="piece postcard-back">
    <h1 class="title"><span class="line-top">Nettle</span><span class="line-main">Winter</span><span class="byline">A film by Ada Nwosu</span></h1>
    <div class="divider"></div>
    <p class="credits"><b>Quiet Field Pictures</b> presents a film by <b>Ada Nwosu</b> 'Nettle Winter'<br>cinematographer <b>Irena Sowa</b> production designer <b>Daniel Osei Mensah</b><br>original music by <b>Karl Weidner</b> edited by <b>Paul Marchand</b> executive producer <b>Nkem Obi</b><br>executive producers <b>Efe Tobore, Ngozi Tobore, Samuel Tobore,</b><br><b>Kemi Tobore, Tunde Ade, Ibim Dagogo, Sotonye Dagogo</b> producer <b>Ada Nwosu</b><br>and <b>Ola Tobore</b> director/writer <b>Ada Nwosu</b></p>
    <div class="partners"><span><i></i>Lensworks</span><span><i></i>Darkroom</span><span><i></i>Huelab</span><span><i></i>Quiet Field</span></div>
  </section>

</main>
</body>
</html>
```